Redesign current business card for food company

i would like to redesign my business card. our company is food company, our product range from chips, juices, milk and etc (mostly dried food stuff).
I want o keep same logo but , the rest is open to new design.
you can check at our website about our company www.velqorafare.com

Target Market(s)

most of food company

Industry/Entity Type

Business

Contact Information for Business Card

I want to keep more to blue color...

Colors
3176b5
abd036

Requirements
Must have
• our old logo
Nice to have
• we do not mind to have nice material on bus card in order to accomplish nice design. for example: using spot uv, embossed and etc.

```html
<!DOCTYPE html>
<html lang="en">
<head>
<meta charset="utf-8">
<title>Velqora Business Card</title>
<link href="https://fonts.googleapis.com/css2?family=Source+Sans+3:wght@400;600;700&display=swap" rel="stylesheet">
<style>
  :root {
    --brand-blue: #3176b5;
    --card-blue: #2a78b8;
    --leaf-green: #abd036;
    --paper: #ffffff;
    --backdrop: #e4e5e8;
  }
  * { margin: 0; padding: 0; box-sizing: border-box; }
  html, body {
    width: 1200px; height: 800px; overflow: hidden;
    background: var(--backdrop);
    font-family: "Source Sans 3", "Myriad Pro", sans-serif;
  }
  .canvas {
    width: 1200px; height: 800px;
    display: flex; align-items: center; justify-content: center; gap: 40px;
  }
  .card {
    position: relative;
    width: 540px; height: 309px;
    border-radius: 2px;
    box-shadow: 0 2px 6px rgba(0,0,0,0.12);
  }
  /* Front */
  .card--front {
    background: var(--card-blue);
    display: flex; align-items: center; justify-content: center;
  }
  .wordmark {
    font-weight: 700;
    letter-spacing: -1px;
    line-height: 1;
  }
  .card--front .wordmark {
    color: var(--paper);
    font-size: 78px;
  }
  /* Back */
  .card--back { background: var(--paper); color: var(--brand-blue); }
  .brand {
    position: absolute; left: 40px; top: 30px;
  }
  .brand__row { display: flex; align-items: flex-start; gap: 6px; }
  .brand .wordmark { color: var(--brand-blue); font-size: 52px; }
  .brand__dot {
    width: 12px; height: 12px; border-radius: 50%;
    background: var(--leaf-green); margin-top: 6px;
  }
  .brand__company {
    font-size: 13px; margin-top: 4px; letter-spacing: 0.2px;
  }
  .person {
    position: absolute; left: 40px; top: 196px;
  }
  .person__name { font-size: 18px; font-weight: 600; }
  .person__title { font-size: 13px; color: var(--leaf-green); margin-top: 2px; }
  .timeline {
    position: absolute; left: 316px; top: 40px;
  }
  .contact {
    position: absolute; left: 362px;
    font-size: 13.5px; line-height: 1.3;
  }
  .contact--address { top: 100px; }
  .contact--phone { top: 160px; }
  .contact--web { top: 220px; }
</style>
</head>
<body>
<main class="canvas">
  <section class="card card--front" aria-label="Business card front">
    <span class="wordmark">velqora</span>
  </section>

  <section class="card card--back" aria-label="Business card back">
    <div class="brand">
      <div class="brand__row">
        <span class="wordmark">velqora</span>
        <span class="brand__dot"></span>
      </div>
      <p class="brand__company">Velqora Enterprises Corp.</p>
    </div>

    <div class="person">
      <p class="person__name">Marcus Delvane</p>
      <p class="person__title">President</p>
    </div>

    <svg class="timeline" width="30" height="240" viewBox="0 0 30 240" aria-hidden="true">
      <line x1="15" y1="2" x2="15" y2="238" stroke="#3176b5" stroke-width="2"/>
      <circle cx="15" cy="2" r="2.5" fill="#3176b5"/>
      <circle cx="15" cy="238" r="2.5" fill="#3176b5"/>
      <!-- address: pin -->
      <circle cx="15" cy="77" r="13" fill="#fff" stroke="#3176b5" stroke-width="2"/>
      <path d="M15 86 C11 80 9.5 77 9.5 74.5 A5.5 5.5 0 0 1 20.5 74.5 C20.5 77 19 80 15 86 Z" fill="#abd036"/>
      <circle cx="15" cy="74.5" r="2" fill="#fff"/>
      <!-- phone -->
      <circle cx="15" cy="137" r="13" fill="#fff" stroke="#3176b5" stroke-width="2"/>
      <path d="M10.5 130.5 l3 -1 l2 4 l-2 1.5 c0.8 2.2 2.3 3.7 4.5 4.5 l1.5 -2 l4 2 l-1 3 c-6 1 -13 -6 -12 -12 z" fill="#abd036"/>
      <!-- web: signal waves -->
      <circle cx="15" cy="197" r="13" fill="#fff" stroke="#3176b5" stroke-width="2"/>
      <circle cx="10.5" cy="202" r="1.8" fill="#abd036"/>
      <path d="M10 196.5 a6 6 0 0 1 6 6" fill="none" stroke="#abd036" stroke-width="2"/>
      <path d="M10 192 a10 10 0 0 1 10 10" fill="none" stroke="#abd036" stroke-width="2"/>
    </svg>

    <p class="contact contact--address">2418 W Orchard Ave.<br>Fairlane CA 90412</p>
    <p class="contact contact--phone">555 214 0187<br>555 382 7740</p>
    <p class="contact contact--web">www.velqorafare.com<br>marcus@velqorafare.com</p>
  </section>
</main>
</body>
</html>
```